Flyer-Design für Geburtstagsglückwunsch-Postkarte
Zielgruppe
Unter www.velkaroutes.de bieten wir im Großraum Stuttgart Städtereisen in europäische Metropolen an (hauptsächlich mit dem Bus), außerdem Eventreisen, Erlebnisreisen, Strandreisen und im Winter Skiausfahrten und Silvesterreisen sowie ganzjährig Gruppenreisen für Vereine und Betriebe an. Zielgruppe recht gemischt vorwiegend jung (18-40 Jahre), Ansprache auf Website und im Schriftverkehr mit 'Sie'. Anbei unser Logo.
Aufgabenstellung
Wir möchten unseren Kunden zum Geburtstag eine Postkarte (Klassisches Format DIn6 148 x 105) senden. Voderseite bunt (schönes Bild + Happy Birthday + velkaroutes wünscht Ihnen alles Gute zum Geburtstag, unser Logo, evtl. www.velkaroutes.de > klein) und Rückseite mit Glückwünschen in s/w (rechts platz für Postkarte oben und anschrift des Kunden > wird von uns handschriftlich hinzugefügt // links dann nette Geburtstagsglückwünsche bereits gedruckt und klein unsere Anschrift velkaroutes GmbH, www.velkaroutes.de). Für Ihre Ideen für eine schöne innovative Geburtstags-Postkarte sind wir offen.

```html
<!DOCTYPE html>
<html lang="de">
<head>
<meta charset="utf-8">
<title>velkaroutes – Geburtstagspostkarte</title>
<link rel="stylesheet" href="https://fonts.googleapis.com/css2?family=Kalam:wght@400;700&family=Chewy&family=Open+Sans:wght@400;600&display=swap">
<style>
  :root {
    --bg: #e9e7e4;
    --paper: #ffffff;
    --ink: #333333;
    --ink-soft: #555555;
    --line: #1f1f1f;
    --rule: #c8c8c8;
    --stamp: #e2e2e2;
    --brand: #1f6fb5;
    --sky: #cfe9f5;
    --pink: #f3c7dc;
    --sun: #f6d743;
    --grass: #8cc63f;
    --hb-red: #e8483b;
    --hb-purple: #8e5bb5;
    --hb-orange: #f28c28;
  }
  * { box-sizing: border-box; margin: 0; padding: 0; }
  html, body { width: 1200px; height: 576px; overflow: hidden; }
  body {
    background: var(--bg);
    display: flex;
    align-items: center;
    justify-content: center;
    gap: 40px;
    font-family: "Open Sans", sans-serif;
  }
  .postcard {
    position: relative;
    width: 540px;
    height: 383px;
    background: var(--paper);
    box-shadow: 0 2px 10px rgba(0,0,0,.15);
    overflow: hidden;
  }

  /* back side */
  .back__message {
    position: absolute;
    left: 0; top: 0;
    width: 270px; height: 100%;
    text-align: center;
    color: var(--ink);
  }
  .brand {
    display: flex;
    flex-direction: column;
    align-items: center;
    gap: 6px;
    margin-top: 34px;
  }
  .brand__dot {
    width: 30px; height: 30px;
    border-radius: 50%;
    border: 2px solid var(--ink);
  }
  .brand__name {
    font-family: "Open Sans", sans-serif;
    font-weight: 600;
    font-size: 14px;
    color: var(--ink);
  }
  .greeting {
    font-family: "Kalam", cursive;
    font-size: 15px;
    line-height: 1.3;
    margin-top: 14px;
  }
  .sender {
    position: absolute;
    left: 0; right: 0; bottom: 36px;
    font-size: 11px;
    line-height: 1.35;
    color: var(--ink-soft);
  }
  .back__divider {
    position: absolute;
    left: 290px; top: 110px;
    width: 4px; height: 160px;
    background: var(--line);
  }
  .back__stamp {
    position: absolute;
    right: 22px; top: 20px;
    width: 66px; height: 80px;
    background: var(--stamp);
  }
  .back__address {
    position: absolute;
    left: 320px; right: 24px; top: 150px;
    display: flex; flex-direction: column; gap: 32px;
  }
  .back__address span { height: 1px; background: var(--rule); }

  /* front side */
  .front__art {
    position: absolute; inset: 0;
    background: linear-gradient(160deg, var(--sky) 0%, var(--pink) 45%, var(--sun) 80%, var(--grass) 100%);
  }
  .front__panel { position: absolute; inset: 0; }
  .front__title {
    position: absolute;
    left: 70px; top: 215px;
    font-family: "Chewy", cursive;
    font-size: 52px;
    line-height: 0.95;
    text-shadow: 2px 2px 0 #fff;
  }
  .front__title .happy { color: var(--hb-red); display: block; }
  .front__title .birthday { color: var(--hb-purple); display: block; padding-left: 14px; }
  .front__brand {
    position: absolute;
    right: 40px; bottom: 82px;
    display: flex; align-items: center; gap: 8px;
  }
  .front__brand .brand__dot { border-color: var(--brand); width: 26px; height: 26px; }
  .front__brand .brand__name { color: var(--brand); font-size: 20px; }
  .front__slogan {
    position: absolute;
    right: 30px; bottom: 30px;
    font-family: "Kalam", cursive;
    font-size: 15px;
    line-height: 1.2;
    color: var(--ink);
    text-align: left;
  }
</style>
</head>
<body>

  <section class="postcard postcard--back" aria-label="Rückseite">
    <div class="back__message">
      <div class="brand">
        <span class="brand__dot"></span>
        <span class="brand__name">velkaroutes</span>
      </div>
      <p class="greeting">Herzlichen Glückwunsch<br>zum Geburtstag!<br>Möge Ihnen das neue Lebensjahr<br>Glück, Gesundheit, sowie<br>viele schöne Momente bringen!</p>
      <address class="sender">
        velkaroutes GmbH<br>
        Lindenweg 17<br>
        71000 Musterstadt<br>
        Tel. 0700 1234567-10<br>
        www.velkaroutes.de
      </address>
    </div>
    <div class="back__divider"></div>
    <div class="back__stamp"></div>
    <div class="back__address"><span></span><span></span><span></span></div>
  </section>

  <section class="postcard postcard--front" aria-label="Vorderseite">
    <div class="front__art" role="img" aria-label="Bunte Illustration: Geburtstagstorte mit Kerzen, Hochhäuser einer Stadt und ein lächelnder blauer Reisebus auf einer Straße"></div>
    <svg class="front__panel" viewBox="0 0 540 383" aria-hidden="true">
      <path d="M250 383 C 300 300, 420 250, 540 240 L540 383 Z" fill="#ffffff"/>
    </svg>
    <h1 class="front__title"><span class="happy">Happy</span><span class="birthday">Birthday</span></h1>
    <div class="front__brand">
      <span class="brand__dot"></span>
      <span class="brand__name">velkaroutes</span>
    </div>
    <p class="front__slogan">Das Leben ist eine Reise…<br>Entdecken Sie neue Ziele.</p>
  </section>

</body>
</html>
```